Halden Decor Services Requires a New Responsive Site

Hi Designers,

Our current website is this www.haldendecor.com.au for some idea.
I made it on Adobe Muse, its very basic.
I would like it to be redesigned to look more professional and also responsive. I actually know how to do html5 and css but I think others will do this much better than me.

I do not need content because I am a copywriter and would like to do all SEO and copy myself.

The most improtant things to remember is that the site cannot use a CMS
and the code needs to be understandable so that I can go in and add content later on and do SEO work.

Also the site requires an additional testimonial page. I would imagine a nice gallery would be a great addition too(something that I can add images too through html. Also in it is important for it to contain those brand images on the front page as it increases authority. I will attach them onto the brief.

Those two files of nearlisted and bluefolders are local directories where we have reviews so a placement of those on the testimonail page would make great sense. I will to the href myself.

Anyway, good luck!

I look forward to see your designs :D
Updates

I have just been informed that on this site websites are simply designed and not built (developed) if this is the case please stop working on your designs and spending more time on this project. I REQUIRE DEVELOPMENT ALSO AND HAVE ALREADY CONTACTED SUPPORT.

Target Market(s)

The target market is 30-75 high income earners.

Industry/Entity Type

Painting

Number of Pages Required

5+ page

Font styles to use
Serif
Sans Serif

Requirements
Must have
• attractive gallery, and the brand icons uploaded.
• must be responsive
• web carousel (with the different types of work we do). eg domestic, commercial, industrial etc.
Nice to have
• a little interactivity
• corporate a natural design that goes well with our logo
Should not have
• any content. just write jiberish to fill in the spaces.
• I will be doing all copy and SEO myself.
• More than five pages, bascially the four that already exist plus the testimonail one.

```html
<!DOCTYPE html>
<html lang="en">
<head>
<meta charset="utf-8">
<title>Halden Decor Services</title>
<link href="https://fonts.googleapis.com/css2?family=Roboto+Condensed:ital,wght@0,400;0,700;1,400&family=Roboto+Slab:wght@400;700&family=Arimo:wght@400&display=swap" rel="stylesheet">
<style>
  :root {
    --top-blue: #0272bd;
    --nav-blue: #5dbbec;
    --nav-active: #c6ebfc;
    --band-blue: #c0e2f6;
    --heading-blue: #3a7ca5;
    --ink: #111111;
    --white: #ffffff;
    --header-bg: #f4f4f4;
    --side-bg: #eeeeee;
    --footer-bg: #dcdcde;
    --rule: #a9a9a9;
    --badge: #1d3e78;
  }
  * { box-sizing: border-box; margin: 0; padding: 0; }
  html, body { width: 999px; height: 1200px; overflow: hidden; }
  body {
    position: relative;
    background: var(--side-bg);
    color: var(--ink);
    font-family: "Roboto Condensed", Arial, sans-serif;
  }
  .abs { position: absolute; }

  .call-bar {
    left: 0; top: 0; width: 999px; height: 41px;
    background: var(--top-blue);
    color: var(--white);
    font-family: "Arimo", Arial, sans-serif;
    font-size: 25px; line-height: 41px;
    padding-left: 55px;
  }

  .site-header {
    left: 0; top: 41px; width: 999px; height: 153px;
    background: var(--header-bg);
    display: flex; align-items: center; justify-content: center; gap: 30px;
  }
  .brand-word {
    font-family: "Roboto Condensed", Arial, sans-serif;
    font-weight: 700; font-size: 33px; letter-spacing: 0.5px;
    color: var(--ink);
  }
  .brand-mark { width: 100px; height: 92px; background: var(--heading-blue); }

  .main-nav {
    left: 0; top: 194px; width: 999px; height: 53px;
    background: var(--nav-blue);
  }
  .nav-item {
    position: absolute; top: 0; height: 53px; line-height: 53px;
    font-size: 21px; color: var(--ink); transform: translateX(-50%);
    white-space: nowrap;
  }
  .nav-item.is-active {
    left: 55px; width: 88px; transform: none; text-align: center;
    background: var(--nav-active); color: var(--top-blue);
  }

  .content-panel {
    left: 42px; top: 247px; width: 915px; height: 588px;
    background: var(--white);
  }

  .hero-slider {
    left: 55px; top: 279px; width: 891px; height: 352px;
    border: 1px solid #bbbbbb;
    background: linear-gradient(180deg, #5f8fd0 0%, #9dbbe2 22%, #e4e6ea 42%, #c9ccd2 62%, #8e8f8a 80%, #4b4a3e 100%);
    overflow: hidden;
  }
  .slider-arrow { position: absolute; top: 156px; }
  .slider-arrow.prev { left: 48px; }
  .slider-arrow.next { left: 800px; }
  .slide-title {
    position: absolute; left: 0; width: 100%; top: 218px; text-align: center;
    font-family: "Roboto Slab", Georgia, serif; font-weight: 700;
    font-size: 34px; color: var(--white); white-space: nowrap;
  }
  .slide-text {
    position: absolute; left: 0; width: 100%; top: 256px; text-align: center;
    font-size: 20px; line-height: 22px; color: var(--white);
  }
  .slide-dots { position: absolute; top: 321px; left: 364px; display: flex; gap: 19px; }
  .slide-dots span { width: 6px; height: 6px; border-radius: 50%; background: var(--white); }

  .section-title {
    left: 61px; top: 676px;
    font-family: "Roboto Slab", Georgia, serif; font-weight: 700;
    font-size: 24px; color: var(--heading-blue); white-space: nowrap;
  }
  .section-rule { left: 57px; top: 713px; width: 872px; height: 1px; background: var(--rule); }
  .intro-text {
    left: 62px; top: 729px; font-size: 14px; line-height: 22px; white-space: nowrap;
  }

  .testimonial-band {
    left: 0; top: 835px; width: 999px; height: 154px;
    background: var(--band-blue);
  }
  .testimonial-heading {
    left: 99px; top: 838px;
    font-family: "Roboto Slab", Georgia, serif; font-weight: 700; font-size: 15px;
    white-space: nowrap;
  }
  .testimonial-text {
    left: 99px; top: 863px;
    font-style: italic; font-size: 13.5px; line-height: 22px;
    white-space: nowrap;
  }
  .read-more {
    left: 99px; top: 970px;
    font-family: "Roboto Slab", Georgia, serif; font-weight: 700;
    font-size: 14px; line-height: 16px; color: var(--heading-blue); white-space: nowrap;
  }

  .site-footer {
    left: 0; top: 1010px; width: 999px; height: 190px;
    background: var(--footer-bg);
  }
  .partner {
    position: absolute; top: 1040px; transform: translateX(-50%);
    font-family: "Roboto Condensed", Arial, sans-serif; font-weight: 700;
    font-size: 22px; color: #333333;
  }
  .partner-badge {
    left: 787px; top: 1025px; width: 52px; height: 58px;
    background: var(--badge); border-radius: 4px;
  }
  .contact-line {
    top: 1114px;
    font-family: "Roboto Slab", Georgia, serif; font-size: 15px; white-space: nowrap;
  }
  .contact-line b { font-weight: 700; }
  .footer-rule { left: 99px; top: 1155px; width: 838px; height: 1px; background: var(--rule); }
  .copyright { left: 97px; top: 1165px; font-size: 10px; }
</style>
</head>
<body>
  <div class="abs call-bar">CALL US TODAY: 1300 555 214</div>

  <header class="abs site-header">
    <span class="brand-word">HALDEN</span>
    <span class="brand-mark"></span>
    <span class="brand-word">DECOR</span>
  </header>

  <nav class="abs main-nav">
    <span class="nav-item is-active">Home</span>
    <span class="nav-item" style="left:227px">Services</span>
    <span class="nav-item" style="left:357px">Gallery</span>
    <span class="nav-item" style="left:508px">Testimonials</span>
    <span class="nav-item" style="left:676px">Contact Us</span>
  </nav>

  <div class="abs content-panel"></div>

  <section class="abs hero-slider" role="img" aria-label="Photo of a large white weatherboard two-storey house with balconies under a blue sky">
    <svg class="slider-arrow prev" width="42" height="42" viewBox="0 0 42 42">
      <circle cx="21" cy="21" r="19" fill="rgba(0,0,0,0.15)" stroke="#fff" stroke-width="2.5"/>
      <path d="M26 11 L13 21 L26 31 Z" fill="#fff"/>
    </svg>
    <svg class="slider-arrow next" width="48" height="48" viewBox="0 0 48 48">
      <circle cx="24" cy="24" r="22" fill="rgba(0,0,0,0.15)" stroke="#fff" stroke-width="2.5"/>
      <path d="M19 12 L34 24 L19 36 Z" fill="#fff"/>
    </svg>
    <div class="slide-title">DOMESTIC PAINTING</div>
    <div class="slide-text">At halden decor we are focused on superior quality and<br>workmanship.</div>
    <div class="slide-dots"><span></span><span></span><span></span></div>
  </section>

  <h2 class="abs section-title">QUALITY SERVICE</h2>
  <div class="abs section-rule"></div>
  <p class="abs intro-text">Halden Decor is an Australian family owned Painting &amp; Decorating business based in Elmsdale, in the south east of Melbourne.<br>We proudly provide domestic and commercial painting services across all suburbs of metropolitan Melbourne.</p>

  <section class="abs testimonial-band"></section>
  <h3 class="abs testimonial-heading">WHAT OUR CUSTOMERS HAVE TO SAY</h3>
  <p class="abs testimonial-text">Lorem ipsum dolor sit amet, consectetuer adipiscing elit. Aenean commodo ligula eget dolor. Aenean massa. Cum sociis natoque penatibus et<br>magnis dis parturient montes, nascetur ridiculus mus. Donec quam felis, ultricies nec, pellentesque eu, pretium quis, sem. Nulla consequat massa<br>quis enim. Donec pede justo, fringilla vel, aliquet nec, vulputate eget, arcu. In enim justo, rhoncus ut, imperdiet a, venenatis vitae, justo. Nullam dictum felis eu<br>pede mollis pretium. Integer tincidunt.</p>
  <span class="abs read-more">READ MORE &gt;&gt;</span>

  <footer class="abs site-footer"></footer>
  <span class="partner" style="left:170px">Corvell</span>
  <span class="partner" style="left:397px">Wrenly</span>
  <span class="partner" style="left:604px">Tasmer</span>
  <div class="abs partner-badge"></div>

  <p class="abs contact-line" style="left:98px"><b>Address:</b>&nbsp; <b>Elmsdale Victoria 3990, Australia</b></p>
  <p class="abs contact-line" style="left:557px"><b>Email:</b>&nbsp; <b>info@haldendecor.com.au</b></p>
  <div class="abs footer-rule"></div>
  <p class="abs copyright">© 2014 Halden Decor. All rights reserved.</p>
</body>
</html>
```